Quillstone Business Card

We need a business card design. We have a logo from a previous Sketchfold project and I am attaching the logo files in jpeg and photoshop.

```html
<!DOCTYPE html>
<html lang="en">
<head>
<meta charset="utf-8">
<title>Quillstone Business Card</title>
<link rel="stylesheet" href="https://fonts.googleapis.com/css2?family=Anton&display=swap">
<style>
  :root {
    --card-bg: #1c1c1c;
    --brand-green: #4bb34a;
    --text-white: #ffffff;
    --name-grey: #dedede;
    --icon-light: #f2f2f2;
  }
  html, body {
    margin: 0;
    padding: 0;
    overflow: hidden;
    background: var(--card-bg);
  }
  .card {
    position: relative;
    width: 1200px;
    height: 702px;
    background: var(--card-bg);
    overflow: hidden;
    font-family: "Anton", Impact, sans-serif;
    color: var(--text-white);
  }
  .brand {
    position: absolute;
    left: 84px;
    top: 196px;
    display: flex;
    align-items: center;
    gap: 26px;
  }
  .brand-square {
    width: 78px;
    height: 78px;
    background: var(--brand-green);
  }
  .brand-name {
    font-size: 100px;
    line-height: 1;
    color: var(--text-white);
    letter-spacing: 1px;
  }
  .person {
    position: absolute;
    left: 761px;
    top: 70px;
  }
  .person-name {
    margin: 0;
    font-size: 47px;
    font-weight: 400;
    line-height: 1.1;
    color: var(--name-grey);
  }
  .person-role {
    margin: 2px 0 0 6px;
    font-size: 26px;
    line-height: 1.2;
    color: var(--text-white);
  }
  .contact-band {
    position: absolute;
    left: 0;
    top: 551px;
    width: 1200px;
    height: 94px;
    background: var(--brand-green);
  }
  .contact-item {
    position: absolute;
    display: flex;
    align-items: center;
    font-size: 27px;
    line-height: 1;
    color: var(--text-white);
  }
  .contact-item svg {
    position: absolute;
    fill: none;
    stroke: var(--icon-light);
    stroke-width: 2;
  }
  .contact-address { left: 93px; top: 560px; }
  .contact-address svg { left: -34px; top: 1px; }
  .contact-phone { left: 515px; top: 560px; }
  .contact-phone svg { left: -32px; top: 0; }
  .contact-fax { left: 524px; top: 600px; }
  .contact-fax svg { left: -42px; top: 2px; }
  .contact-email { left: 848px; top: 560px; }
  .contact-email svg { left: -56px; top: 6px; }
  .contact-web { left: 848px; top: 598px; }
  .contact-web svg { left: -56px; top: 3px; }
</style>
</head>
<body>
  <main class="card">
    <div class="brand">
      <span class="brand-square"></span>
      <span class="brand-name">Quillstone</span>
    </div>

    <div class="person">
      <h1 class="person-name">Name and Surname</h1>
      <p class="person-role">Your position</p>
    </div>

    <div class="contact-band"></div>

    <div class="contact-item contact-address">
      <svg width="26" height="26" viewBox="0 0 26 26"><path d="M3 13 L13 3 L23 13 M6 11 V23 H11 V16 H15 V23 H20 V11" fill="#f2f2f2" stroke="#f2f2f2"/></svg>
      Address
    </div>
    <div class="contact-item contact-phone">
      <svg width="24" height="28" viewBox="0 0 24 28"><path d="M6 3 L10 8 L7 11 C8 15 11 19 14 21 L17 18 L21 23 L17 26 C9 23 4 14 3 6 Z"/></svg>
      00 123 123 123
    </div>
    <div class="contact-item contact-fax">
      <svg width="26" height="26" viewBox="0 0 26 26"><rect x="7" y="2" width="12" height="10"/><rect x="2" y="12" width="22" height="11"/><line x1="6" y1="18" x2="20" y2="18"/></svg>
      Fax
    </div>
    <div class="contact-item contact-email">
      <svg width="24" height="18" viewBox="0 0 24 18"><rect x="1" y="1" width="22" height="15"/><path d="M1 1 L12 10 L23 1"/></svg>
      your@email.com
    </div>
    <div class="contact-item contact-web">
      <svg width="24" height="24" viewBox="0 0 24 24"><circle cx="12" cy="12" r="10"/><path d="M2 12 H22 M12 2 C7 7 7 17 12 22 M12 2 C17 7 17 17 12 22"/></svg>
      www.yourwebsite.com
    </div>
  </main>
</body>
</html>
```